Wen Foyle Book Cover Design Project

I would like a book cover design for a science fiction book tentatively entitled "Last Orbiter" by Wendell K Foyle II.

The book opens with a scene in the foothills of the Blue Ridge Valley:

"Riding alone on a crisp December morning, Gil Ashcombe suddenly and uncharacteristically curses. For the fifth time in as many rides, Ashcomb’s Zuvo had delivered the same anonymous message—this time paradoxically following The Copper Hinges’ Lantern in the Quarry. The message simply said: “Dr. Ashcombe, I’m a messenger from God. He has a mission for you. Please meet me at noon on Christmas day in the videoconference room at your school. Come alone. More will be revealed.”

I imagine a cover showing the Blue Ridge Mountains, but could be convince otherwise.

Target Market(s)

Highly educated readers struggling to reconcile science and faith.

Industry/Entity Type

School

Requirements
Must have
• Book Title
Author's Name
Nice to have
• Blue Ridge Mountain scene

```html
<!DOCTYPE html>
<html lang="en">
<head>
<meta charset="utf-8">
<title>Last Orbiter — Book Cover</title>
<link rel="stylesheet" href="https://fonts.googleapis.com/css2?family=Open+Sans:wght@300;400&display=swap">
<style>
  :root {
    --stage: #b9b9b9;
    --stage-edge: #8d8d8d;
    --sky-light: #6d9fe0;
    --sky-mid: #3f74c4;
    --sky-deep: #2a559f;
    --ridge-top: #27386f;
    --ridge-mid: #1b2756;
    --ridge-deep: #131b42;
    --glow-core: rgba(200, 222, 255, 0.38);
    --glow-edge: rgba(120, 165, 235, 0);
    --author: #8ea3c9;
    --title: #cddcf3;
  }

  * { box-sizing: border-box; margin: 0; padding: 0; }

  html, body {
    width: 1200px;
    height: 842px;
    overflow: hidden;
  }

  body {
    background: radial-gradient(ellipse at 50% 40%, var(--stage) 0%, var(--stage-edge) 100%);
    font-family: "Open Sans", Arial, sans-serif;
    position: relative;
  }

  .book-cover {
    position: absolute;
    left: 340px;
    top: 41px;
    width: 520px;
    height: 760px;
    overflow: hidden;
    background: var(--ridge-deep);
    box-shadow: 0 12px 30px rgba(0, 0, 0, 0.35);
  }

  .cover-art {
    position: absolute;
    inset: 0;
    width: 100%;
    height: 100%;
    display: block;
  }

  .emblem-area {
    position: absolute;
    left: 150px;
    top: 100px;
    width: 170px;
    height: 175px;
    background: radial-gradient(ellipse at 50% 50%, var(--glow-core) 0%, var(--glow-edge) 70%);
  }

  .cover-credits {
    position: absolute;
    right: 34px;
    top: 446px;
    text-align: right;
  }

  .author-name {
    font-weight: 400;
    font-size: 17px;
    letter-spacing: 0.6px;
    color: var(--author);
    line-height: 1;
  }

  .book-title {
    font-weight: 300;
    font-size: 44px;
    letter-spacing: 0.5px;
    color: var(--title);
    line-height: 1.05;
    margin-top: 2px;
  }
</style>
</head>
<body>
  <main class="book-cover">
    <svg class="cover-art" viewBox="0 0 520 760" role="img"
         aria-label="Blue circuit-board texture above a dusky Blue Ridge mountain ridge at twilight">
      <defs>
        <linearGradient id="sky-tone" x1="0" y1="0" x2="1" y2="1">
          <stop offset="0" stop-color="var(--sky-light)"/>
          <stop offset="0.55" stop-color="var(--sky-mid)"/>
          <stop offset="1" stop-color="var(--sky-deep)"/>
        </linearGradient>
        <linearGradient id="ridge-tone" x1="0" y1="0" x2="0" y2="1">
          <stop offset="0" stop-color="var(--ridge-top)"/>
          <stop offset="0.35" stop-color="var(--ridge-mid)"/>
          <stop offset="1" stop-color="var(--ridge-deep)"/>
        </linearGradient>
      </defs>
      <rect class="sky-band" x="0" y="0" width="520" height="260" fill="url(#sky-tone)"/>
      <path class="mountain-ridge"
            d="M0 218 C60 212 110 205 170 200 C230 195 260 186 310 184 C370 182 430 190 470 186 C495 184 510 182 520 181 L520 760 L0 760 Z"
            fill="url(#ridge-tone)"/>
    </svg>

    <div class="emblem-area" role="img"
         aria-label="Glowing outlined triangle emblem with short line accents"></div>

    <header class="cover-credits">
      <p class="author-name">Wendell K Foyle II</p>
      <h1 class="book-title">Last Orbiter</h1>
    </header>
  </main>
</body>
</html>
```